Flyer-Design für Designer-Schmuck
Großartig - sehr gut !! Super zu frieden !!
Zielgruppe
Wir produzieren außergewöhnlichen und hochwertigen Designer-Schmuck aus Lüster-Bleikristallen für eine modebewusstes Publikum. Der Flyer wird als Beipack-Flyer unseren Versendungen beigefügt und enthält Informationen, sowie Hinweise für unsere Kunden über Morgenfalter, zu Nachhaltigkeit und Pflege.
Aufgabenstellung
nicht größer als DIN A5 | mindestens 2 oder mehr Seiten | Sollte die Aufteilung der Texte 6 Seiten erfordern sind auch 6 Seiten in Ordnung | Design und Layout sind sonst wenig Grenzen gesetzt - wir lassen uns gerne von Euren Vorschlägen begeistern, gerne aber mit Wiedererkennungswert zur Webseite https://morgenfalter-hamburg.de

```html
<!DOCTYPE html>
<html lang="de">
<head>
<meta charset="utf-8">
<title>Morgenfalter Hamburg – Beipack-Flyer</title>
<link href="https://fonts.googleapis.com/css2?family=Questrial&family=Roboto+Condensed:wght@400;700&family=Pinyon+Script&display=swap" rel="stylesheet">
<style>
  :root {
    --purple: #8d1f7c;
    --purple-text: #9a2688;
    --paper: #f1f0f1;
    --grey-light: #e3e2e3;
    --grey-mid: #c9c8c9;
    --ink: #4a4a4a;
    --stage: #f3e9f0;
    --white: #ffffff;
  }
  * { box-sizing: border-box; margin: 0; padding: 0; }
  html, body { width: 1200px; height: 900px; overflow: hidden; }
  body {
    background: var(--stage);
    font-family: "Roboto Condensed", Arial, sans-serif;
    color: var(--ink);
    position: relative;
  }
  .spread {
    position: absolute;
    left: 45px;
    width: 1110px;
    height: 405px;
    display: flex;
    box-shadow: 0 6px 22px rgba(90, 40, 80, .18);
  }
  .spread--outside { top: 30px; }
  .spread--inside { top: 465px; }
  .panel {
    position: relative;
    width: 370px;
    height: 100%;
    overflow: hidden;
  }
  .heading {
    font-family: "Questrial", "Century Gothic", sans-serif;
    color: var(--purple-text);
    font-weight: 400;
    font-size: 15px;
    line-height: 1.2;
  }
  .script {
    font-family: "Pinyon Script", cursive;
    font-weight: 400;
  }
  .body-text { font-size: 8.6px; line-height: 1.45; }
  .body-text p + p { margin-top: 9px; }
  .image-slot { position: absolute; }

  /* outside: intro panel */
  .panel--intro { background: var(--paper); padding: 42px 32px 0 34px; }
  .panel--intro .heading { margin-bottom: 14px; }
  .panel--intro .bracelet {
    left: 0; top: 270px; width: 190px; height: 110px;
    background: radial-gradient(ellipse at 50% 55%, #e9d6da 0%, #dcdcdc 55%, var(--paper) 80%);
  }
  .panel--intro .quote {
    position: absolute; right: 30px; top: 272px; width: 130px;
    text-align: right; font-style: italic; font-size: 8.6px; line-height: 1.45;
    color: var(--purple-text);
  }

  /* outside: contact panel */
  .panel--contact { background: var(--paper); }
  .panel--contact .colour-block {
    position: absolute; left: 0; top: 0; width: 100%; height: 205px; background: var(--purple);
  }
  .panel--contact .contact {
    position: absolute; left: 150px; top: 230px; width: 200px;
  }
  .panel--contact .heading { margin-bottom: 12px; }
  .panel--contact .web { color: var(--purple-text); font-size: 9px; margin: 12px 0 14px; }

  /* outside: cover */
  .panel--cover { background: linear-gradient(var(--grey-mid) 0 54%, var(--purple) 54% 100%); }
  .panel--cover .portrait {
    left: 38px; top: 55px; width: 290px; height: 330px;
    background: linear-gradient(135deg, #5a5a5a 0%, #2a2a2a 45%, #7a7a7a 100%);
  }
  .brand-tag {
    position: absolute; left: 142px; top: 10px; width: 90px; height: 132px;
    background: var(--grey-mid);
    display: flex; flex-direction: column; align-items: center; justify-content: flex-end;
    padding-bottom: 14px;
  }
  .brand-tag .brand-dot { width: 22px; height: 22px; border-radius: 50%; background: var(--purple); margin-bottom: 12px; }
  .brand-tag .brand-name { font-family: "Questrial", sans-serif; color: var(--purple); font-size: 12px; }
  .brand-tag .brand-city { font-family: "Questrial", sans-serif; color: var(--purple); font-size: 8px; letter-spacing: .6px; }
  .cover-claim {
    position: absolute; left: 200px; top: 212px; width: 120px;
    color: var(--white); font-family: "Questrial", sans-serif; font-size: 12px; line-height: 1.3;
  }
  .cover-claim .script { display: block; text-align: right; font-size: 17px; line-height: 1.05; margin-top: 4px; }

  /* inside: overview */
  .panel--overview { background: linear-gradient(180deg, #d6d5d6 0%, var(--paper) 60%, #dcdbdc 100%); padding: 28px 0 0 34px; }
  .panel--overview .script { color: var(--purple-text); font-size: 20px; display: block; margin: 2px 0 14px 14px; }
  .panel--overview .list { list-style: none; width: 170px; font-size: 8.8px; line-height: 1.35; }
  .panel--overview .list li { position: relative; padding-left: 9px; margin-top: 6px; }
  .panel--overview .list li::before { content: "•"; position: absolute; left: 0; }
  .panel--overview .pendant {
    left: 225px; top: 10px; width: 90px; height: 240px;
    background: linear-gradient(180deg, #e4e4e4 0%, #bdbdbd 45%, #5b3c9a 80%, #e9e8e9 100%);
  }
  .panel--overview .earrings {
    left: 30px; top: 285px; width: 100px; height: 110px;
    background: linear-gradient(180deg, #dcdcdc 0%, #bcbcbc 50%, #8d1a2a 85%, #e1e0e1 100%);
  }
  .panel--overview .note {
    position: absolute; right: 26px; top: 325px; width: 200px;
    text-align: right; font-size: 6.5px; line-height: 1.45;
  }

  /* inside: sustainability */
  .panel--sustain { background: var(--purple); color: var(--white); padding: 36px 0 0 28px; }
  .panel--sustain .heading { color: var(--white); font-size: 14px; margin-bottom: 16px; }
  .panel--sustain .intro { width: 200px; }
  .panel--sustain .necklace-end {
    left: 250px; top: 25px; width: 120px; height: 110px;
    background: radial-gradient(ellipse at 40% 50%, rgba(230,230,230,.85) 0%, rgba(200,200,200,.4) 45%, rgba(141,31,124,0) 75%);
  }
  .panel--sustain .col { position: absolute; width: 150px; list-style: none; }
  .panel--sustain .col li { position: relative; padding-left: 10px; margin-bottom: 8px; }
  .panel--sustain .col li::before { content: "•"; position: absolute; left: 0; }
  .panel--sustain .col--left { left: 28px; top: 140px; }
  .panel--sustain .col--right { left: 200px; top: 195px; width: 150px; }
  .panel--sustain .outro { position: absolute; left: 210px; top: 300px; width: 145px; }

  /* inside: care */
  .panel--care { background: linear-gradient(var(--paper) 0 81%, var(--grey-light) 81% 100%); }
  .panel--care .necklace {
    left: 0; top: 10px; width: 370px; height: 150px;
    background: radial-gradient(ellipse at 40% 55%, #ececec 0%, #d9d9d9 40%, var(--paper) 72%);
  }
  .panel--care .title { position: absolute; right: 30px; top: 85px; text-align: right; }
  .panel--care .title .script { display: block; color: var(--purple-text); font-size: 20px; }
  .panel--care .body-text { position: absolute; right: 30px; top: 150px; width: 250px; text-align: right; }
  .panel--care .note { position: absolute; left: 26px; top: 340px; width: 200px; font-size: 6.5px; line-height: 1.45; }
</style>
</head>
<body>

<section class="spread spread--outside">
  <article class="panel panel--intro">
    <h2 class="heading">Einzigartige, luxuriöse Schmuckstücke für dich</h2>
    <div class="body-text">
      <p>Mit den Schmuckstücken von Morgenfalter Hamburg bewahrst du einen Teil einer magisch anmutenden Vergangenheit und bringst zugleich Eleganz und Luxus in deinen Alltag.</p>
      <p>Sicher kennst du die großen, glitzernden Kronleuchter, die in prunkvollen Schlössern hängen und ihre Umgebung mit Schönheit, Glanz und Freude füllen. Seit Generationen begleiten und faszinieren sie uns, tragen Geheimnisse und Geschichten in sich und haben besondere Momente miterlebt.</p>
      <p>Diesen Glanz und diese Erinnerung an die Geschichten alter Zeiten fangen wir in den individuell gefertigten Miniatur-Lüstern ein, welche die meisten der Morgenfalter-Schmuckstücke zieren. Zusätzlich wählen wir mit großer Sorgfalt einzelne Kristalle aus und verarbeiten beide Elemente zu edlen, wahrlich einzigartigen Schmuckstücken.</p>
    </div>
    <div class="image-slot bracelet" role="img" aria-label="Silbernes Armband mit rosa, roten und klaren Kristalltropfen"></div>
    <p class="quote">Ob kraftvoll in intensiven Farben oder zeitlos und dezent: Mit Morgenfalter wird dein Leben ein bisschen mystischer, luxuriöser oder einfach schöner – unsere Art, unsere Liebe zum Lüster mit dir zu teilen.</p>
  </article>

  <article class="panel panel--contact">
    <div class="colour-block"></div>
    <div class="contact">
      <h2 class="heading">Lerne uns kennen</h2>
      <p class="body-text">Auf unserer Website findest du unser gesamtes Sortiment – zum Beispiel edle Halsketten, elegante Ohrringe und verspielte Armbänder. Wir freuen uns auf deinen Besuch!</p>
      <p class="web">www.morgenfalter-hamburg.de</p>
      <p class="body-text">Tel: +49 151-48 20 17 35<br>E-Mail: info@morgenfalter.de</p>
    </div>
  </article>

  <article class="panel panel--cover">
    <div class="image-slot portrait" role="img" aria-label="Schwarz-Weiß-Porträt einer Frau mit großem Hut und Kristallschmuck"></div>
    <div class="brand-tag">
      <span class="brand-dot"></span>
      <span class="brand-name">Morgenfalter</span>
      <span class="brand-city">HAMBURG</span>
    </div>
    <p class="cover-claim">Liebevoll gefertigte Schmuckstücke,<span class="script">so einzigartig<br>wie du.</span></p>
  </article>
</section>

<section class="spread spread--inside">
  <article class="panel panel--overview">
    <h2 class="heading">Die Morgenfalter-<br>Schmuckstücke</h2>
    <span class="script">auf einen Blick</span>
    <p class="body-text" style="width:170px">Die graziösen Schmuckstücke von Morgenfalter Hamburg</p>
    <ul class="list">
      <li>werden von Hand gearbeitet</li>
      <li>sind unverwechselbare Einzelstücke</li>
      <li>werden aus echten Kristallen und 925er Sterlingsilber hergestellt</li>
      <li>erreichen dich in einem speziellen Glas zur schonenden Aufbewahrung</li>
      <li>werden unter hohen Anforderungen an Nachhaltigkeit produziert</li>
    </ul>
    <div class="image-slot pendant" role="img" aria-label="Silberner Lüster-Anhänger mit violettem Kristalltropfen"></div>
    <div class="image-slot earrings" role="img" aria-label="Ohrringe mit Miniatur-Lüstern und roten Kristalltropfen"></div>
    <p class="note"><strong>Bitte beachte:</strong> Die Kristalle können aufgrund ihres Alters einzelne Gebrauchsspuren aufweisen. Diese sind Teil ihrer Vergangenheit und machen sie nicht weniger schön, sondern verleihen ihnen im Gegenteil eine authentische, lebendige Einzigartigkeit.</p>
  </article>

  <article class="panel panel--sustain body-text">
    <h2 class="heading">Unser Nachhaltigkeitsversprechen</h2>
    <p class="intro">Es ist uns wichtig, unseren Beitrag zu den hohen Klimazielen unseres Landes zu leisten. Deshalb setzen wir bei Morgenfalter Hamburg folgende Maßnahmen für mehr Nachhaltigkeit um:</p>
    <div class="image-slot necklace-end" role="img" aria-label="Silberkette mit Kristalltropfen und Perlen"></div>
    <ul class="col col--left">
      <li>Unsere Schmuckstücke bestehen zum großen Teil aus wiederverwendeten Kristallen.</li>
      <li>Die Fassung in Form eines Lüsters wird regional angefertigt.</li>
      <li>Das dekorative Morgenfalterglas kannst du auch anderweitig nutzen, um weitere Lieblingsstücke aufzubewahren, oder du kannst es wie gewohnt recyceln.</li>
      <li>Die Schmuckplatten, auf denen du deine Schmuckstücke erhältst, sind aus Acryl gegossen. Wenn du sie nicht benötigst, kannst du sie an uns zurücksenden. Wir verwenden sie dann als Muster oder für Ausstellungsstücke.</li>
    </ul>
    <ul class="col col--right">
      <li>Alle Versandkartons bestehen aus recyceltem Altpapier oder aus Secondhand-Kartonage.</li>
      <li>Gravuren führen wir selbst durch – dadurch entfallen unnötige Transportwege.</li>
    </ul>
    <p class="outro">Wir verbessern unsere Prozesse immer weiter, sodass du deine Morgenfalter-Schmuckstücke nicht nur aus Freude, sondern auch mit gutem Gewissen tragen</p>
  </article>

  <article class="panel panel--care">
    <div class="image-slot necklace" role="img" aria-label="Silberkette mit klaren Kristalltropfen und Perlen"></div>
    <h2 class="heading title">Pflegetipps und<span class="script">Sicherheitshinweise</span></h2>
    <div class="body-text">
      <p>Jedes Schmuckstück kommt im dekorativen Morgenfalterglas zu dir, das eine luftdichte Aufbewahrung ermöglicht und Schutz vor äußeren Einflüssen bietet. So bleiben die Schönheit und der Glanz deiner Schmuckstücke lange erhalten.</p>
      <p>Ist das Silber doch einmal angelaufen, kannst du ein Silberputztuch oder ein Silberbad verwenden, um es wieder strahlen zu lassen. Die Kristalle werden dadurch nicht geschädigt. Nur Perlen müssen vorher abgenommen werden. Wende dich bei Fragen gern an uns!</p>
    </div>
    <p class="note"><strong>Wichtig:</strong> Da die Schmuckstücke verschluckbare Kleinteile enthalten, bewahre sie bitte außerhalb der Reichweite von Kindern unter drei Jahren auf. Kristall und Glas sind zerbrechlich und müssen vor Stoß und Schlag geschützt werden.</p>
  </article>
</section>

</body>
</html>
```